MediDesk 4.2 is web based clinic management software. We require 1 logo for the software product, login page design and landing page (patient queue) design. The design should include all elements required logo, icons , buttons and type faces. http://md2021.tralvonix.my/Default.aspxTest login : KQ417 password : 4826 Final output should be in psd for developer to convert to css for web application.

Number of Pages Required

1 page

Colors

Designer to choose colors to be used in the design.

Requirements
Must have
• Product Logo , icon, login page design, and 1 main page design as attached.

```html
<!DOCTYPE html>
<html lang="en">
<head>
<meta charset="utf-8">
<title>MediDesk 4.2 – Login and Patients Queue</title>
<link href="https://fonts.googleapis.com/css2?family=Roboto:wght@300;400;500&display=swap" rel="stylesheet">
<style>
:root{
  --navy:#2433b6;
  --blue:#1f6fe0;
  --sky:#2aa6f2;
  --ink:#2d3440;
  --muted:#8a919c;
  --line:#e3e6eb;
  --panel:#f4f6f9;
  --white:#ffffff;
  --page:#fbfbfc;
}
*{box-sizing:border-box;margin:0;padding:0}
html,body{width:887px;height:1200px;overflow:hidden;background:var(--white);font-family:'Roboto',sans-serif;color:var(--ink)}
.canvas{position:relative;width:887px;height:1200px}
.section-label{position:absolute;left:18px;font-size:13px;color:var(--ink)}
.screen{position:absolute;left:18px;width:851px;background:var(--page);border:1px solid var(--line)}
.brand{position:absolute;font-size:22px;font-weight:300;color:var(--blue);letter-spacing:.2px}
.btn{display:flex;align-items:center;justify-content:center;background:var(--navy);color:var(--white);font-size:11px;border-radius:2px}
.btn-top{position:absolute;right:20px;width:90px;height:24px}
/* login */
.login-card{position:absolute;left:272px;top:90px;width:308px;height:214px;background:var(--white);box-shadow:0 2px 10px rgba(0,0,0,.12)}
.card-head{height:40px;background:linear-gradient(90deg,var(--blue),var(--sky));color:var(--white);font-size:15px;padding:11px 16px}
.field{margin:16px 20px 0;border-bottom:1px solid var(--line);font-size:8px;color:var(--muted);padding-bottom:10px}
.login-opts{display:flex;justify-content:space-between;margin:14px 20px 0;font-size:8px;color:var(--muted)}
.login-opts .check{display:flex;align-items:center;gap:4px}
.box{width:8px;height:8px;border:1px solid var(--muted);display:inline-block}
.link{color:var(--blue)}
.login-btn{width:82px;height:22px;margin:18px auto 0}
/* footer */
.footer{position:absolute;left:0;right:0;border-top:1px solid var(--line);padding:12px 20px 0}
.footer h4{font-size:14px;font-weight:400;color:var(--blue)}
.footer h4 span{color:var(--ink);font-weight:300}
.footer p{font-size:6.5px;color:var(--muted);line-height:10px}
.footer .contact{position:absolute;left:20px;top:12px;width:300px}
.footer .links{position:absolute;left:552px;top:12px}
.footer .more{position:absolute;left:712px;top:12px}
.footer .gap{margin-top:6px}
.copyright{position:absolute;left:0;right:0;bottom:0;border-top:1px solid var(--line);font-size:6.5px;color:var(--muted);padding:7px 20px;height:22px}
/* queue page */
.sidebar{position:absolute;left:0;top:0;width:116px;bottom:0;border-right:1px solid var(--line);background:var(--white)}
.nav{position:absolute;top:64px;left:0;right:0;list-style:none}
.nav li{display:flex;align-items:center;gap:7px;height:24px;padding-left:14px;font-size:9px;color:var(--ink)}
.nav li.active{background:var(--blue);color:var(--white)}
.nav li svg{width:10px;height:10px}
.nav .group{margin-top:14px;font-size:7px;color:var(--muted);height:18px}
.main{position:absolute;left:116px;top:0;right:0;bottom:0}
.page-title{position:absolute;left:20px;top:18px;font-size:11px}
.user-btn{position:absolute;right:20px;top:14px;width:78px;height:22px}
.meta{position:absolute;left:20px;top:48px;right:20px;display:flex;gap:18px;border-bottom:1px solid var(--line);padding-bottom:8px}
.meta div{width:140px;font-size:6.5px;color:var(--muted);border-bottom:1px solid var(--line);padding-bottom:4px}
.meta b{display:block;font-weight:400;font-size:8px;color:var(--ink);margin-top:3px}
.meta .opt{display:flex;align-items:flex-end;gap:4px;border:none}
.queue-card{position:absolute;left:20px;top:100px;right:20px;height:178px;background:var(--white);box-shadow:0 2px 8px rgba(0,0,0,.1)}
.queue-card .card-head{height:46px;font-size:16px;padding:14px 18px}
.toolbar{display:flex;align-items:center;justify-content:space-between;margin:12px 18px 0}
.search{width:300px;height:20px;border:1px solid var(--line);border-radius:2px;font-size:7px;color:var(--muted);display:flex;align-items:center;gap:5px;padding-left:6px}
.new-btn{width:78px;height:20px}
table{width:calc(100% - 36px);margin:14px 18px 0;border-collapse:collapse;font-size:7px}
th{font-weight:500;text-align:left;padding:5px 4px;border-bottom:1px solid var(--line)}
td{padding:7px 4px;color:var(--ink);background:var(--panel)}
.actions{display:flex;gap:7px}
.actions svg{width:9px;height:9px}
.pager{font-size:7px;color:var(--muted);margin:10px 18px 0}
</style>
</head>
<body>
<div class="canvas">

  <div class="section-label" style="top:8px">1) Login page</div>
  <section class="screen login-screen" style="top:26px;height:474px">
    <div class="brand" style="left:20px;top:20px">MediDesk</div>
    <div class="btn btn-top" style="top:20px">Sign Up</div>

    <div class="login-card">
      <div class="card-head">Login</div>
      <div class="field">Username</div>
      <div class="field">Password</div>
      <div class="login-opts">
        <span class="check"><span class="box"></span>Remember me</span>
        <span class="link">Forgot Password?</span>
      </div>
      <div class="btn login-btn">Login</div>
    </div>

    <footer class="footer" style="top:324px;height:150px">
      <div class="contact">
        <h4>Contact <span>us</span></h4>
        <p class="gap">TEL +603-5512 7840 / +603-5512 7841</p>
        <p>FAX +603-5512 7842 / +603-5512 7843</p>
        <p class="gap">No. 12, Jalan Teratai 5, Taman Seri Indah, 47100 Puchong, Selangor, Malaysia</p>
        <p class="gap">Tel: +603-5512 7844 / +603-5512 7845</p>
        <p>Fax: +603-5512 7846</p>
        <p>Email: hello@medidesk.example</p>
      </div>
      <div class="links">
        <h4>Links</h4>
        <p class="gap">Link 1</p><p>Link 2</p><p>Link 3</p><p>Link 4</p><p>Link 5</p>
      </div>
      <div class="more">
        <h4>More <span>Links</span></h4>
        <p class="gap">Clinic hours and days</p><p>Nearby branches</p><p>Help and support</p>
      </div>
      <div class="copyright">©2018 Copyright MediDesk</div>
    </footer>
  </section>

  <div class="section-label" style="top:510px">2) Patients queue page</div>
  <section class="screen queue-screen" style="top:528px;height:664px">
    <aside class="sidebar">
      <div class="brand" style="left:14px;top:20px;font-size:19px">MediDesk</div>
      <ul class="nav">
        <li><svg viewBox="0 0 10 10"><rect x="1" y="1" width="8" height="8" fill="none" stroke="currentColor"/></svg>Queue</li>
        <li class="active"><svg viewBox="0 0 10 10"><circle cx="5" cy="3.5" r="2" fill="currentColor"/><path d="M1 9.5c0-2.5 8-2.5 8 0" fill="currentColor"/></svg>Patient</li>
        <li><svg viewBox="0 0 10 10"><path d="M2 1h6v8H2z M3.5 3h3 M3.5 5h3" fill="none" stroke="currentColor"/></svg>Visit Entry</li>
        <li><svg viewBox="0 0 10 10"><rect x="1" y="2.5" width="8" height="5" fill="none" stroke="currentColor"/></svg>Payment</li>
        <li class="group">Maintenance</li>
        <li>Clinic information</li>
        <li>Branch information</li>
        <li class="group">General</li>
        <li><svg viewBox="0 0 10 10"><path d="M6 2H2v6h4 M4.5 5H9 M7.5 3.5L9 5 7.5 6.5" fill="none" stroke="currentColor"/></svg>Logout</li>
      </ul>
    </aside>

    <div class="main">
      <div class="page-title">Patients Queue List</div>
      <div class="btn user-btn">Sam Rowe</div>
      <div class="meta">
        <div>Queue Date<b>10.07.2018</b></div>
        <div>Location<b>Any Location</b></div>
        <div class="opt"><span class="box"></span>Display by doctor</div>
      </div>

      <div class="queue-card">
        <div class="card-head">Queue List</div>
        <div class="toolbar">
          <div class="search"><svg width="8" height="8" viewBox="0 0 10 10"><circle cx="4" cy="4" r="3" fill="none" stroke="#8a919c"/><path d="M6.5 6.5L9 9" stroke="#8a919c"/></svg>Listing of patients in a queue</div>
          <div class="btn new-btn">New Queue</div>
        </div>
        <table>
          <thead><tr><th>No</th><th>PatientName</th><th>Time</th><th>Payer</th><th>Amount</th><th>Room</th><th>Location</th><th></th></tr></thead>
          <tbody><tr>
            <td>1</td><td>AMIRA ZAINAL</td><td>09:10 AM</td><td>Self</td><td>RM 48.00</td><td>R1</td><td>Main</td>
            <td><div class="actions">
              <svg viewBox="0 0 10 10"><path d="M1 9l1-3 5-5 2 2-5 5z" fill="#2d3440"/></svg>
              <svg viewBox="0 0 10 10"><rect x="2" y="1" width="6" height="8" fill="#2d3440"/></svg>
              <svg viewBox="0 0 10 10"><path d="M8 5a3 3 0 1 1-1-2.2M7 1v2h-2" fill="none" stroke="#2d3440"/></svg>
              <svg viewBox="0 0 10 10"><path d="M2 3h6l-1 6H3z M1.5 2h7M4 1h2" fill="none" stroke="#2d3440"/></svg>
            </div></td>
          </tr></tbody>
        </table>
        <div class="pager">Page 1 of 1</div>
      </div>

      <footer class="footer" style="top:300px;bottom:0;padding-left:20px">
        <div class="contact">
          <h4>Contact <span>us</span></h4>
          <p class="gap">TEL +603-5512 7840 / +603-5512 7841</p>
          <p>FAX +603-5512 7842 / +603-5512 7843</p>
          <p class="gap">No. 12, Jalan Teratai 5, Taman Seri Indah, 47100 Puchong, Selangor</p>
          <p class="gap">Tel: +603-5512 7844 / +603-5512 7845</p>
          <p>Fax: +603-5512 7846</p>
          <p>Email: hello@medidesk.example</p>
        </div>
        <div class="links" style="left:436px">
          <h4>Links</h4>
          <p class="gap">Link 1</p><p>Link 2</p><p>Link 3</p><p>Link 4</p><p>Link 5</p>
        </div>
        <div class="more" style="left:596px">
          <h4>More <span>Links</span></h4>
          <p class="gap">Clinic hours and days</p><p>Nearby branches</p><p>Help and support</p>
        </div>
        <div class="copyright">©2018 Copyright MediDesk</div>
      </footer>
    </div>
  </section>

</div>
</body>
</html>
```